Cedarbrook Residences - Billboard design for our newly renovated townhome community

We have a 5' wide x 4' tall billboard at the entrance to our apartment community, that needs to have the acrylic insert replaced. It is a 2 sided sign, and we are planning to use the same image on both sides. We are called Cedarbrook Residences, and have 48 townhomes that are all 2 bedroom, 1 1/2 bath. A few things we would like to get across on the signage: "Newly Renovated" "2 bed 1 1/2 bath" "Full size W/D in every home" " New Appliances" I've included our parent company's logo - this is the only image I could think of, but it might not be worth having it on the sign. We are in Colorado, so mountain theme could be nice and also sunshine/sun since we are called "Cedarbrook"

Industry/Entity Type

Apartment

Font styles to use
Sans Serif

Requirements
Must have
• Newly Renovated
2 bed 1 1/2 bath
Full size W/D in every home
Virtual Tours available
www.marlowepeaksliving.com
855 - 413 - 9268
Nice to have
• We are located in Colorado - possibly mountain theme? Since our community is called "Cedarbrook Residences" - anything bright with Sun / Sunshine might look really nice as well.

```html
<!DOCTYPE html>
<html lang="en">
<head>
<meta charset="UTF-8">
<title>Cedarbrook Residences – Newly Renovated Sign</title>
<link rel="stylesheet" href="https://fonts.googleapis.com/css2?family=Montserrat:wght@500;600;700;800;900&display=swap">
<style>
  :root {
    --page-bg: #e4e4e4;
    --sky-top: #e97a3c;
    --sky-mid: #e2552a;
    --sky-low: #cf2a1e;
    --sky-base: #c3141a;
    --sun-glow: #f2b63c;
    --white: #ffffff;
    --ink: #1a1a1a;
    --logo-ink: #4a4a4a;
    --phone-yellow: #f8ea00;
    --shadow: rgba(70, 10, 0, 0.45);
  }
  * { margin: 0; padding: 0; box-sizing: border-box; }
  html, body {
    width: 1200px;
    height: 1200px;
    overflow: hidden;
    background: var(--page-bg);
    font-family: "Montserrat", sans-serif;
  }
  .sign {
    position: absolute;
    left: 40px;
    top: 195px;
    width: 1120px;
    height: 810px;
    overflow: hidden;
  }
  .sign__sky {
    position: absolute;
    inset: 0;
    background:
      radial-gradient(circle at 17% 22%, var(--sun-glow) 0, rgba(242,182,60,0.75) 110px, rgba(242,182,60,0) 200px),
      linear-gradient(180deg, var(--sky-top) 0%, var(--sky-mid) 48%, var(--sky-low) 75%, var(--sky-base) 100%);
  }
  .sign__frame {
    position: absolute;
    inset: 0;
  }
  .brand-badge {
    position: absolute;
    left: 334px;
    top: 0;
    width: 452px;
    height: 226px;
  }
  .brand-badge__name {
    position: absolute;
    left: 0;
    right: 0;
    top: 128px;
    text-align: center;
    font-weight: 600;
    font-size: 25px;
    color: var(--logo-ink);
  }
  .headline {
    position: absolute;
    left: 0;
    right: 0;
    text-align: center;
    color: var(--white);
    font-weight: 900;
    line-height: 1;
    text-shadow: 4px 6px 8px var(--shadow);
  }
  .headline--newly { top: 250px; font-size: 118px; letter-spacing: 1px; }
  .headline--renovated { top: 372px; font-size: 118px; letter-spacing: 0; }
  .features {
    position: absolute;
    left: 128px;
    top: 507px;
    width: 842px;
    height: 60px;
    background: var(--white);
    box-shadow: 10px 10px 0 var(--ink);
    display: flex;
    align-items: center;
    justify-content: center;
    gap: 16px;
    font-weight: 800;
    font-size: 25px;
    color: var(--ink);
    white-space: nowrap;
  }
  .features__divider { font-weight: 700; }
  .phone {
    position: absolute;
    left: 0;
    right: 0;
    top: 604px;
    text-align: center;
    font-weight: 800;
    font-size: 120px;
    line-height: 1;
    color: var(--phone-yellow);
    text-shadow: 4px 6px 8px var(--shadow);
  }
  .footer-line {
    position: absolute;
    left: 0;
    right: 0;
    top: 746px;
    text-align: center;
    font-weight: 600;
    font-size: 23px;
    color: var(--white);
  }
</style>
</head>
<body>
  <main class="sign" aria-label="Cedarbrook Residences newly renovated townhomes sign">
    <div class="sign__sky" role="img" aria-label="Sunset sky with a glowing sun, drifting clouds, birds and rolling red hills"></div>

    <svg class="sign__frame" width="1120" height="810" viewBox="0 0 1120 810" aria-hidden="true">
      <g fill="none" stroke="#ffffff" stroke-width="5">
        <polyline points="334,43 49,43 49,768 172,768"/>
        <polyline points="786,43 1067,43 1067,768 932,768"/>
      </g>
    </svg>

    <div class="brand-badge">
      <svg width="452" height="226" viewBox="0 0 452 226" aria-hidden="true">
        <defs>
          <linearGradient id="badgeFill" x1="0" y1="0" x2="0" y2="1">
            <stop offset="0" stop-color="#f1f1f1"/>
            <stop offset="0.25" stop-color="#ffffff"/>
            <stop offset="1" stop-color="#ffffff"/>
          </linearGradient>
        </defs>
        <polygon points="0,0 452,0 452,188 226,226 0,188" fill="url(#badgeFill)"/>
      </svg>
      <div class="brand-badge__name">Ridgeline Property Group</div>
    </div>

    <h1 class="headline headline--newly">NEWLY</h1>
    <h1 class="headline headline--renovated">RENOVATED</h1>

    <div class="features">
      <span>2 BED</span>
      <span class="features__divider">|</span>
      <span>1 1/2 BATH</span>
      <span class="features__divider">|</span>
      <span>FULL SIZE W/D IN EVERY HOME</span>
    </div>

    <p class="phone">855-413-9268</p>

    <p class="footer-line">Virtual Tours available | www.marlowepeaksliving.com</p>
  </main>
</body>
</html>
```